New band called Velorance, 1 lead female singer, 3 male musicians.

I called my band Velorance as we are all from different backgrounds and hold many secrets. We are mysterious in our own ways, hence the name Velorance. I am looking for a design that shows quite the nice over exaggerated cursive writing to be seen as feminine but I also want us to have that 'bad ass' image as well to represent the boys in the band. As I am the lead singer, it needs to show some sense of female lead presence. We sing a lot of pop like, Dana Whitlow, Mona Brisk, V!OX, Tamsin R but I also sing stuff from Corinne Haldavey and Renata holm. So we are very diverse. I dont want a 'pop' look but a mix between urban and punk/rock? Whatever the design is for our cards I'd like to also use for a banner in the background to hang on stage and to also be versatile to possibly use for posters and shirts also. I have a copy of a drawing/sketch that has been done. I like the writing but not 100% on the pic of the girl thats used. Love blues and purples also. I will try wear these colours when doing a gig.
Reason: Band members are having difficulty deciding on one design. Extending deadline to provide designers the chance to make any additional changes we may have.
Industry/Entity Type
Singer
Contact Information for Business Card
Velorance, Live music, contact JoN on 0461937208 for bookings. Also cater for functions, weddings and other special events.
Logo Text
Velorance

```html
<!DOCTYPE html>
<html lang="en">
<head>
<meta charset="utf-8">
<title>Velorance – Live music</title>
<link rel="stylesheet" href="https://fonts.googleapis.com/css2?family=Great+Vibes&display=swap">
<style>
  :root {
    --deep-blue: #1631a6;
    --royal-blue: #1f4fc2;
    --teal-glow: #1ec4c9;
    --aqua: #27a7d0;
    --ink-white: #ffffff;
    --placeholder-light: #e9eef7;
    --placeholder-dark: #20242e;
  }
  html, body {
    margin: 0;
    padding: 0;
    width: 1200px;
    height: 693px;
    overflow: hidden;
    background: var(--deep-blue);
  }
  .business-card {
    position: relative;
    width: 1200px;
    height: 693px;
    overflow: hidden;
    background:
      radial-gradient(ellipse 420px 330px at 640px 250px, rgba(30,196,201,0.95), rgba(30,196,201,0) 100%),
      linear-gradient(90deg, var(--deep-blue) 0%, var(--royal-blue) 30%, var(--aqua) 52%, var(--royal-blue) 78%, var(--deep-blue) 100%);
    font-family: "Great Vibes", cursive;
    color: var(--ink-white);
  }
  .music-notes-backdrop {
    position: absolute;
    left: 480px;
    top: 20px;
    width: 720px;
    height: 540px;
    border-radius: 50%;
    background: radial-gradient(ellipse at 55% 55%, rgba(120,170,230,0.25), rgba(120,170,230,0) 70%);
  }
  .singer-illustration {
    position: absolute;
    left: 17px;
    top: 34px;
    width: 383px;
    height: 508px;
    border-radius: 46% 40% 30% 30% / 30% 30% 20% 20%;
    background: linear-gradient(115deg, var(--placeholder-dark) 0%, var(--placeholder-dark) 30%, var(--placeholder-light) 55%, var(--placeholder-light) 100%);
  }
  .band-name {
    position: absolute;
    left: 280px;
    top: 40px;
    width: 880px;
    margin: 0;
    text-align: center;
    font-weight: 400;
    font-size: 210px;
    line-height: 330px;
    color: var(--ink-white);
  }
  .tagline {
    position: absolute;
    left: 878px;
    top: 362px;
    margin: 0;
    font-size: 48px;
    line-height: 56px;
    text-shadow: 0 0 6px rgba(255,255,255,0.5);
  }
  .booking-info {
    position: absolute;
    left: 0;
    top: 560px;
    width: 1200px;
    margin: 0;
    text-align: center;
    font-size: 44px;
    line-height: 50px;
    text-shadow: 0 0 6px rgba(255,255,255,0.45);
  }
  .booking-info span { display: block; }
</style>
</head>
<body>
  <main class="business-card">
    <div class="music-notes-backdrop" role="img" aria-label="Faint decorative treble clef and music notes"></div>
    <div class="singer-illustration" role="img" aria-label="Illustration of a female lead singer holding a microphone"></div>
    <h1 class="band-name">Velorance</h1>
    <p class="tagline">Live music</p>
    <p class="booking-info">
      <span>Contact JoN on 0461937208 for bookings</span>
      <span>Also cater for functions, weddings and other special events</span>
    </p>
  </main>
</body>
</html>
```